We need a business card design for a new company based in
Perth, Western Australia called Bexom Tiling Services. We specialize in laying Wall and Floor Tiles and Stone. We expertise in all small to large format tiles and do good quality work. Sincerity and Convition is what seperates us from others.

```html
<!DOCTYPE html>
<html lang="en">
<head>
<meta charset="utf-8">
<title>Bexom Tiling Services – Business Card</title>
<link rel="stylesheet" href="https://fonts.googleapis.com/css2?family=Source+Sans+3:wght@400&display=swap">
<style>
  :root {
    --page-bg: #e4e4e5;
    --card-black: #000000;
    --brand-green: #8dc63f;
    --brand-grey: #96979a;
    --label-grey: #9a9a9a;
    --ink: #111111;
    --white: #ffffff;
    --font-main: "Source Sans 3", "Myriad Pro", Arial, sans-serif;
  }
  * { margin: 0; padding: 0; box-sizing: border-box; }
  html, body {
    width: 886px; height: 1200px; overflow: hidden;
    background: var(--page-bg);
    font-family: var(--font-main);
  }
  .canvas { position: relative; width: 886px; height: 1200px; }

  .card {
    position: absolute; left: 16px; width: 850px; height: 484px;
    overflow: hidden;
    box-shadow: 0 6px 10px rgba(0,0,0,0.25);
  }
  .card__art { position: absolute; inset: 0; width: 100%; height: 100%; }

  .card--front { top: 50px; background: var(--card-black); }
  .card--back { top: 631px; }

  .brand {
    position: absolute; display: flex; align-items: center;
    font-weight: 400; white-space: nowrap;
  }
  .brand__mark { display: block; flex: none; }
  .card--front .brand { left: 72px; top: 210px; color: var(--white); font-size: 38px; gap: 36px; }
  .card--front .brand__mark { width: 34px; height: 34px; background: var(--white); }
  .card--back .brand { left: 84px; top: 198px; color: var(--ink); font-size: 54px; gap: 50px; }
  .card--back .brand__mark { width: 46px; height: 46px; background: var(--ink); }

  .contact {
    position: absolute; left: 557px; top: 225px;
    color: var(--white); font-size: 22px; line-height: 27px;
  }
  .contact__name { font-size: 26px; line-height: 32px; }
  .contact__label { color: var(--label-grey); }
  .contact__web { color: var(--brand-green); }

  .about {
    position: absolute; left: 190px; top: 305px;
    color: var(--ink); font-size: 19px; line-height: 24px;
    letter-spacing: 0.15px; white-space: nowrap;
  }
</style>
</head>
<body>
<main class="canvas">

  <section class="card card--front" aria-label="Business card front">
    <svg class="card__art" viewBox="0 0 850 484" aria-hidden="true">
      <polygon points="0,0 122,122 0,245" fill="var(--brand-green)"/>
      <polygon points="0,245 120,363 0,484" fill="var(--brand-grey)"/>
    </svg>

    <div class="brand">
      <span class="brand__mark"></span>
      <span class="brand__name">Bexom Tiling Services</span>
    </div>

    <div class="contact">
      <p class="contact__name">Dean Marlow</p>
      <p><span class="contact__label">Phone</span> 458 902 3XX</p>
      <p><span class="contact__label">E-mail</span> info@bexomtiling.com</p>
      <p class="contact__web">www.bexomtiling.com</p>
    </div>
  </section>

  <section class="card card--back" aria-label="Business card back">
    <svg class="card__art" viewBox="0 0 850 484" aria-hidden="true">
      <defs>
        <linearGradient id="steel" x1="0" y1="0" x2="1" y2="0">
          <stop offset="0.15" stop-color="#f2f2f3"/>
          <stop offset="0.45" stop-color="#d4d5d7"/>
          <stop offset="0.75" stop-color="#909195"/>
          <stop offset="1" stop-color="#3a3b3d"/>
        </linearGradient>
        <linearGradient id="green-fade" gradientUnits="userSpaceOnUse" x1="0" y1="0" x2="500" y2="0">
          <stop offset="0" stop-color="#8dc63f"/>
          <stop offset="0.4" stop-color="#a8d06e"/>
          <stop offset="1" stop-color="#dde0da"/>
        </linearGradient>
      </defs>
      <rect width="850" height="484" fill="url(#steel)"/>
      <polygon points="0,0 124,0 608,484 0,484" fill="url(#green-fade)"/>
    </svg>

    <div class="brand">
      <span class="brand__mark"></span>
      <span class="brand__name">Bexom Tiling Services</span>
    </div>

    <div class="about">
      <p>We specialize in laying Wall and Floor Tiles and Stone.</p>
      <p>We are experts in all small to large format tiles and do good quality work.</p>
      <p>Sincerity and Conviction is what seperates us from others.</p>
    </div>
  </section>

</main>
</body>
</html>
```